Automotive component supplier needs a business card design

We need a business card design for our company called Velmar Global Components Ltd based in the UK. We are a supplier of interior and exterior components to premium car manufacturers such as Corvane Hale, Durrant Fyfe, Maxtorn and Valdessimo. We would like to see a modern business card design that uses the colour blue.

Target Market(s)

Premium automotive car manufacturers.

Industry/Entity Type

Automotive

Contact Information for Business Card

Company Name : Velmar Global Components Limited
Address: 17 Tamsey Yard, Upper Drisk, Warwick, CV31 8RJ, United Kingdom
Web Address : www.velmarparts-example.co.uk

Font styles to use
Other font styles liked:
• Helvetica

Colors
3176b5
0255a3
85acd3
cfdeed
cee9f5
85cae6
34a6d7
0692cd
9bcb3c

Requirements
Must have
• Clear company logo and a mixture of blue colours.
Nice to have
• A high quality modern image.
Should not have
• Multiple colours.

```html
<!DOCTYPE html>
<html lang="en">
<head>
<meta charset="utf-8">
<title>Velmar Global Components – Business Card</title>
<link rel="stylesheet" href="https://fonts.googleapis.com/css2?family=Lato:wght@400;700;900&display=swap">
<style>
  :root {
    --brand-blue: #068fcb;
    --deep-blue: #0585c0;
    --accent-green: #9bcb3c;
    --ink: #1a1a1a;
    --paper: #ffffff;
    --backdrop: #efefef;
  }
  * { box-sizing: border-box; margin: 0; padding: 0; }
  html, body { width: 1200px; height: 586px; overflow: hidden; }
  body {
    position: relative;
    background: var(--backdrop);
    font-family: "Lato", Helvetica, Arial, sans-serif;
  }
  .card {
    position: absolute;
    top: 129px;
    width: 501px;
    height: 300px;
    overflow: hidden;
  }
  .card--front { left: 61px; background: var(--brand-blue); }
  .card--back { left: 619px; background: var(--paper); }

  /* Front */
  .front-name {
    position: absolute;
    left: 0; right: 0; top: 112px;
    text-align: center;
    color: var(--paper);
    font-weight: 900;
    font-size: 34px;
    letter-spacing: 0.5px;
  }
  .front-web {
    position: absolute;
    left: 0; right: 0; top: 262px;
    text-align: center;
    color: var(--paper);
    font-size: 11px;
    font-weight: 700;
    letter-spacing: 2.6px;
  }

  /* Back */
  .person { position: absolute; left: 34px; top: 50px; }
  .person__name { color: var(--brand-blue); font-weight: 900; font-size: 16px; }
  .person__role { color: var(--ink); font-size: 13px; margin-top: 2px; }

  .back-name {
    position: absolute;
    right: 29px; top: 40px;
    color: var(--brand-blue);
    font-weight: 900;
    font-size: 20px;
  }
  .partners {
    position: absolute;
    right: 29px; top: 92px;
    font-size: 11.5px;
    font-weight: 700;
    color: var(--ink);
  }
  .partners .sep { color: var(--accent-green); margin: 0 3px; font-weight: 400; }

  .contacts { position: absolute; left: 34px; top: 149px; list-style: none; }
  .contacts li {
    display: flex; align-items: center;
    height: 24.5px;
    font-size: 13px;
    color: var(--ink);
  }
  .contacts svg { width: 14px; height: 14px; margin-right: 7px; fill: var(--brand-blue); }

  .address {
    position: absolute; left: 35px; top: 226px;
    color: var(--brand-blue);
    font-size: 11.5px;
    font-weight: 700;
    line-height: 15px;
    font-style: normal;
  }
  .swoosh { position: absolute; left: 0; top: 0; width: 501px; height: 300px; }
</style>
</head>
<body>

<section class="card card--front">
  <div class="front-name">Velmar Global Components</div>
  <div class="front-web">www.velmarparts-example.co.uk</div>
</section>

<section class="card card--back">
  <svg class="swoosh" viewBox="0 0 501 300" aria-hidden="true">
    <path d="M109 283 Q360 278 501 230 L501 250 Q370 280 109 284 Z" fill="var(--accent-green)"/>
    <path d="M0 288 L140 288 Q380 285 501 257 L501 300 L0 300 Z" fill="var(--brand-blue)"/>
  </svg>

  <div class="person">
    <div class="person__name">Mara Ellison</div>
    <div class="person__role">Director</div>
  </div>

  <div class="back-name">Velmar Global Components</div>

  <div class="partners">
    Corvane Hale<span class="sep">|</span>Durrant Fyfe<span class="sep">|</span>Maxtorn<span class="sep">|</span>Valdessimo
  </div>

  <ul class="contacts">
    <li>
      <svg viewBox="0 0 14 14" aria-hidden="true"><path d="M4 0h6a1 1 0 0 1 1 1v12a1 1 0 0 1-1 1H4a1 1 0 0 1-1-1V1a1 1 0 0 1 1-1zm0.4 1.5v9.5h5.2V1.5zM7 11.6a0.8 0.8 0 1 0 0 1.6a0.8 0.8 0 1 0 0-1.6z"/></svg>
      (000) 555 0143
    </li>
    <li>
      <svg viewBox="0 0 14 14" aria-hidden="true"><path d="M1 4Q7 0 13 4L12 6L9.5 5L9.5 4Q7 3 4.5 4L4.5 5L2 6Z"/><path d="M3 7L5 5.5H9L11 7V12H3Z"/></svg>
      0400 555 0188
    </li>
    <li>
      <svg viewBox="0 0 14 14" aria-hidden="true"><path d="M0 3h14v9H0zM1.2 4.2L7 8.4l5.8-4.2z"/></svg>
      mellison@velmarparts-example.co.uk
    </li>
  </ul>

  <address class="address">
    17 Tamsey Yard, Upper Drisk<br>
    Calvermoor, ZX9 4QT, UK
  </address>
</section>

</body>
</html>
```